Business card design for Bront Engineering Qavo

We need a new business card design along with all the necessary to place an order. The company is Bront Engineering Qavo and we recently updated our logo.

```html
<!DOCTYPE html>
<html lang="en">
<head>
<meta charset="utf-8">
<title>Bront Engineering Qavo — Business Card</title>
<link rel="stylesheet" href="https://fonts.googleapis.com/css2?family=Lexend:wght@400;600&display=swap">
<style>
  :root {
    --stage: #ececec;
    --card: #ffffff;
    --ink: #1e1e1e;
    --brand-grey: #9b9a96;
    --brand-yellow: #e2c500;
  }
  * { margin: 0; padding: 0; box-sizing: border-box; }
  html, body {
    width: 1200px;
    height: 1200px;
    overflow: hidden;
    background: var(--stage);
    font-family: "Lexend", Arial, sans-serif;
    color: var(--ink);
  }
  .card {
    position: absolute;
    left: 181px;
    width: 845px;
    height: 482px;
    background: var(--card);
  }
  .card--front { top: 94px; }
  .card--back { top: 630px; }

  .brand {
    position: absolute;
    display: flex;
    align-items: center;
    gap: 12px;
    transform: translate(-50%, -50%);
    white-space: nowrap;
  }
  .brand__mark {
    width: 18px;
    height: 18px;
    background: var(--brand-yellow);
  }
  .brand__name {
    font-weight: 600;
    color: var(--brand-grey);
    letter-spacing: 0.04em;
    text-transform: uppercase;
  }
  .card--front .brand { left: 422px; top: 243px; }
  .card--front .brand__name { font-size: 34px; }
  .card--back .brand { left: 229px; top: 245px; }
  .card--back .brand__mark { width: 14px; height: 14px; }
  .card--back .brand__name { font-size: 22px; }

  .front__web {
    position: absolute;
    right: 51px;
    top: 424px;
    font-size: 18px;
    letter-spacing: 0.02em;
  }

  .contact {
    position: absolute;
    left: 475px;
    top: 112px;
  }
  .contact__name {
    font-size: 40px;
    font-weight: 600;
    letter-spacing: 0.12em;
    line-height: 1;
  }
  .contact__title {
    margin-top: 6px;
    font-size: 21px;
    font-weight: 600;
  }
  .contact__address {
    margin-top: 16px;
    font-size: 20px;
  }
  .contact__list {
    list-style: none;
    margin-top: 22px;
  }
  .contact__item {
    display: flex;
    align-items: center;
    gap: 18px;
    height: 32px;
    margin-bottom: 9px;
    margin-left: -4px;
    font-size: 21px;
    letter-spacing: 0.04em;
  }
  .contact__item--phone { letter-spacing: 0.14em; }
  .contact__icon { width: 32px; height: 32px; flex: none; }
</style>
</head>
<body>
  <section class="card card--front">
    <div class="brand">
      <span class="brand__mark"></span>
      <span class="brand__name">Bront Engineering Qavo</span>
    </div>
    <p class="front__web">www.yourwebsite.com</p>
  </section>

  <section class="card card--back">
    <div class="brand">
      <span class="brand__mark"></span>
      <span class="brand__name">Bront Engineering Qavo</span>
    </div>

    <div class="contact">
      <h1 class="contact__name">Your Name</h1>
      <p class="contact__title">Your Title</p>
      <p class="contact__address">Your Address and Country</p>
      <ul class="contact__list">
        <li class="contact__item contact__item--phone">
          <svg class="contact__icon" viewBox="0 0 32 32" aria-hidden="true">
            <circle cx="16" cy="16" r="16" fill="var(--brand-yellow)"/>
            <path d="M10 9c1-1 2-1 3 0l2 3c.5 1 0 1.7-.8 2.3.8 1.8 2 3 3.8 3.8.6-.8 1.3-1.3 2.3-.8l3 2c1 1 1 2 0 3-2 2-5 1-8.5-2.5S8 11 10 9z" fill="#fff"/>
          </svg>
          <span>123-456-789</span>
        </li>
        <li class="contact__item">
          <svg class="contact__icon" viewBox="0 0 32 32" aria-hidden="true">
            <circle cx="16" cy="16" r="16" fill="var(--brand-yellow)"/>
            <g fill="none" stroke="#fff" stroke-width="1.4">
              <circle cx="16" cy="16" r="8"/>
              <ellipse cx="16" cy="16" rx="3.5" ry="8"/>
              <path d="M8 16h16M9.5 12h13M9.5 20h13"/>
            </g>
          </svg>
          <span>www.yourwebsite.com</span>
        </li>
        <li class="contact__item">
          <svg class="contact__icon" viewBox="0 0 32 32" aria-hidden="true">
            <circle cx="16" cy="16" r="16" fill="var(--brand-yellow)"/>
            <g fill="none" stroke="#fff" stroke-width="1.4">
              <rect x="8" y="11" width="16" height="11"/>
              <path d="M8 11l8 6 8-6M8 22l6-5M24 22l-6-5"/>
            </g>
          </svg>
          <span>email@info.com</span>
        </li>
      </ul>
    </div>
  </section>
</body>
</html>
```